Meridian Vessel, Inc. - Travel Worldwide
New Biz Cards for Modern Female Run Travel Agency - Travel
New Biz Cards for Modern Female Run Travel Agency
Simple
Loretta Pim, CTC
Owner
Boston, NY, Worldwide
loretta@meridianvessel-example.com
www.meridianvessel-example.com
We will need the same designed biz card for 2 main employees: Loretta Pim, CTC (Owner) loretta@meridianvessel-example.com Tamsin Ulwick, CTA (International Travel Consultant and Lead Planner) tamsin@meridianvessel-example.com
Honeymoons Destination Weddings Luxury Leisure Travel Your personal travel concierge.
MeridianVessel MeridianVessel
Hi plumquarto, thanks for all your submissions. we are reviewing and determining what we like and don't like. FYI what we like: 2 sided designs, clean lines, gray shading what we don't like: 1 sided designs, color fading, swirls/curves, duplicating designs on both sides, overuse of the logo THANK YOU
Hi Gondy, thanks for your submissions. a bit of text that we wanted to be included is missing, however. if you want to resubmit with that text, we have updated it to be: "Luxury Leisure Travel Honeymoons Destination Events Personal Travel Concierge"

```html
<!DOCTYPE html>
<html lang="en">
<head>
<meta charset="utf-8">
<title>Meridian Vessel – Business Cards</title>
<link rel="stylesheet" href="https://fonts.googleapis.com/css2?family=Raleway:wght@300;400&family=Tenor+Sans&display=swap">
<style>
  :root {
    --backdrop: #e6e3df;
    --card-grey: #8e9697;
    --card-white: #f7f7f6;
    --band-grey: #b9c0c1;
    --ink-white: #f4f5f5;
    --ink-grey: #7d8586;
    --ink-dark: #3e4344;
    --ring-light: rgba(255,255,255,0.25);
    --ring-grey: rgba(140,150,152,0.28);
  }
  * { box-sizing: border-box; margin: 0; padding: 0; }
  html, body { width: 1200px; height: 806px; overflow: hidden; }
  body {
    background: var(--backdrop);
    font-family: 'Raleway', sans-serif;
    position: relative;
  }
  .card {
    position: absolute;
    width: 540px;
    height: 300px;
    overflow: hidden;
    box-shadow: 0 3px 10px rgba(0,0,0,0.18);
  }
  .card--front { left: 330px; top: 60px; background: var(--card-grey); color: var(--ink-white); }
  .card--loretta { left: 40px; top: 392px; background: var(--card-white); color: var(--ink-grey); }
  .card--tamsin { left: 620px; top: 392px; background: var(--card-white); color: var(--ink-grey); }

  .decor-ring { position: absolute; border-radius: 50%; }
  .card--front .decor-ring { width: 280px; height: 280px; left: 0; top: -30px; border: 2px solid var(--ring-light); }
  .card--loretta .decor-ring, .card--tamsin .decor-ring {
    width: 220px; height: 220px; right: -30px; top: 80px; border: 2px solid var(--ring-grey);
  }

  .brand { position: absolute; display: flex; align-items: center; gap: 12px; white-space: nowrap; }
  .brand-dot { flex: none; width: 26px; height: 26px; border-radius: 50%; border: 1.5px solid currentColor; }
  .brand-name { font-family: 'Tenor Sans', sans-serif; font-size: 20px; letter-spacing: 5px; text-transform: uppercase; }
  .card--front .brand { left: 0; right: 0; top: 110px; justify-content: center; padding-left: 120px; }
  .card--loretta .brand, .card--tamsin .brand { left: 62px; top: 128px; }
  .card--loretta .brand-name, .card--tamsin .brand-name { font-size: 15px; letter-spacing: 4px; }
  .card--loretta .brand-dot, .card--tamsin .brand-dot { width: 22px; height: 22px; }

  .services { position: absolute; left: 128px; top: 183px; font-size: 13px; line-height: 1.55; }
  .services .sep { margin: 0 7px; }
  .web-front { position: absolute; left: 0; right: 0; top: 246px; text-align: center; font-size: 11px; letter-spacing: 0.5px; }

  .side-band { position: absolute; left: 0; top: 0; width: 34px; height: 100%; background: var(--band-grey); }
  .side-band span {
    position: absolute; left: 50%; top: 50%;
    transform: translate(-50%, -50%) rotate(-90deg);
    font-size: 10px; color: var(--ink-white); white-space: nowrap; letter-spacing: 0.5px;
  }
  .person { position: absolute; right: 22px; top: 22px; text-align: right; }
  .person-name { font-family: 'Tenor Sans', sans-serif; font-size: 19px; color: var(--ink-dark); }
  .person-title { font-size: 10px; color: var(--ink-grey); margin-top: 3px; }
  .contact { position: absolute; left: 56px; top: 218px; font-size: 10.5px; line-height: 1.85; list-style: none; }
  .contact li { display: flex; align-items: center; gap: 6px; }
  .contact svg { width: 10px; height: 10px; fill: var(--ink-grey); }
</style>
</head>
<body>

<section class="card card--front">
  <div class="decor-ring" aria-hidden="true"></div>
  <div class="brand">
    <span class="brand-dot" aria-hidden="true"></span>
    <span class="brand-name">Meridian Vessel</span>
  </div>
  <p class="services">Luxury Leisure Travel<span class="sep">•</span>Honeymoons<span class="sep">•</span>Destination Events<br>Personal Travel Concierge</p>
  <p class="web-front">www.meridianvessel-example.com</p>
</section>

<section class="card card--loretta">
  <div class="side-band"><span>www.meridianvessel-example.com</span></div>
  <div class="decor-ring" aria-hidden="true"></div>
  <div class="person">
    <div class="person-name">Loretta Pim, CTC</div>
    <div class="person-title">Owner</div>
  </div>
  <div class="brand">
    <span class="brand-dot" aria-hidden="true"></span>
    <span class="brand-name">Meridian Vessel</span>
  </div>
  <ul class="contact">
    <li>Boston, NY, Worldwide</li>
    <li><svg viewBox="0 0 10 10"><path d="M2 1h2l1 2.5-1.2.8a5 5 0 0 0 2 2l.8-1.2L9 6v2a1 1 0 0 1-1 1A7 7 0 0 1 1 2a1 1 0 0 1 1-1z"/></svg>508.555.0142</li>
    <li><svg viewBox="0 0 10 10"><circle cx="5" cy="5" r="4.5"/></svg>loretta@meridianvessel-example.com</li>
  </ul>
</section>

<section class="card card--tamsin">
  <div class="side-band"><span>www.meridianvessel-example.com</span></div>
  <div class="decor-ring" aria-hidden="true"></div>
  <div class="person">
    <div class="person-name">Tamsin Ulwick, CTA</div>
    <div class="person-title">International Travel Consultant &amp; Lead Planner</div>
  </div>
  <div class="brand">
    <span class="brand-dot" aria-hidden="true"></span>
    <span class="brand-name">Meridian Vessel</span>
  </div>
  <ul class="contact">
    <li>Boston, NY, Worldwide</li>
    <li><svg viewBox="0 0 10 10"><path d="M2 1h2l1 2.5-1.2.8a5 5 0 0 0 2 2l.8-1.2L9 6v2a1 1 0 0 1-1 1A7 7 0 0 1 1 2a1 1 0 0 1 1-1z"/></svg>508.555.0142</li>
    <li><svg viewBox="0 0 10 10"><circle cx="5" cy="5" r="4.5"/></svg>tamsin@meridianvessel-example.com</li>
  </ul>
</section>

</body>
</html>
```